Label for Custom Gin Botle

Design an label for Gin botle, need label asap sorry

Target Market(s)

Our customers

Requirements
Must have
• Classic/expensive look

```html
<!DOCTYPE html>
<html lang="en">
<head>
<meta charset="utf-8">
<title>Verdam Foundry Gin – Bottle Label</title>
<link href="https://fonts.googleapis.com/css2?family=Bebas+Neue&display=swap" rel="stylesheet">
<style>
  :root {
    --paper: #ffffff;
    --label-bg: #053830;
    --label-bg-soft: #0a4636;
    --brand-green: #009a3f;
    --ink-light: #ffffff;
  }
  html, body {
    margin: 0;
    padding: 0;
    width: 1200px;
    height: 900px;
    overflow: hidden;
    background: var(--paper);
  }
  .canvas {
    display: block;
    width: 1200px;
    height: 900px;
  }
  .label-type {
    font-family: "Bebas Neue", "Oswald", sans-serif;
    fill: var(--ink-light);
  }
  .site-name { font-size: 19px; letter-spacing: 1px; }
  .category { font-size: 40px; letter-spacing: 9px; }
  .spec-line { font-size: 9.5px; letter-spacing: 0.8px; }
  .arch-caption { font-size: 14px; letter-spacing: 3px; }
  .address-line { font-size: 9.5px; letter-spacing: 0.8px; }
  .maker-name { font-size: 44px; letter-spacing: 4px; }
  .product-name { font-size: 96px; letter-spacing: 10px; }
  .product-kind { font-size: 72px; letter-spacing: 8px; }
  .panel-green { fill: var(--brand-green); }
  .warning-icon { fill: none; stroke: var(--ink-light); stroke-width: 1.4; }
</style>
</head>
<body>
<svg class="canvas" viewBox="0 0 1200 900" xmlns="http://www.w3.org/2000/svg">
  <defs>
    <radialGradient id="groundGlow" cx="55%" cy="50%" r="65%">
      <stop offset="0" stop-color="var(--label-bg-soft)"/>
      <stop offset="1" stop-color="var(--label-bg)"/>
    </radialGradient>
    <path id="siteArc" d="M112,279 Q147,262 182,283"/>
    <path id="batchArc" d="M124,498 A22,22 0 0 1 168,498"/>
    <path id="bottleArc" d="M124,572 A22,22 0 0 1 168,572"/>
  </defs>

  <!-- label ground; the art-deco line pattern sits here -->
  <rect class="label-ground" x="45" y="223" width="1109" height="454" fill="url(#groundGlow)"
        role="img" aria-label="Dark green ground with a subtle art-deco line pattern"/>

  <!-- information column -->
  <g class="info-column">
    <text class="label-type site-name"><textPath href="#siteArc" startOffset="50%" text-anchor="middle">VERDAM.EU</textPath></text>
    <text class="label-type category" x="115" y="324">GIN</text>

    <rect class="warning-icon" x="118.5" y="343.5" width="23" height="23"
          role="img" aria-label="Pregnancy warning pictogram"/>
    <rect class="warning-icon" x="118.5" y="373.5" width="23" height="23"
          role="img" aria-label="No drinking and driving pictogram"/>

    <text class="label-type spec-line" x="117" y="424">40% VOL.  |  500ML</text>
    <text class="label-type spec-line" x="116" y="440">KAN SPOREN VAN</text>
    <text class="label-type spec-line" x="116" y="450">ALLERGENEN BEVATTEN</text>

    <path class="panel-green batch-arch" d="M117,524 V496 A29,29 0 0 1 175,496 V524 Z"/>
    <text class="label-type arch-caption"><textPath href="#batchArc" startOffset="50%" text-anchor="middle">BATCH</textPath></text>

    <path class="panel-green bottle-arch" d="M117,599 V570 A29,29 0 0 1 175,570 V599 Z"/>
    <text class="label-type arch-caption"><textPath href="#bottleArc" startOffset="50%" text-anchor="middle">BOTTLE</textPath></text>

    <text class="label-type address-line" x="118" y="623">LINDEWEG 12</text>
    <text class="label-type address-line" x="118" y="633">6822 AB ARNHEM</text>
    <text class="label-type address-line" x="118" y="643">INFO@VERDAM-GIN.COM</text>
  </g>

  <!-- brand name block -->
  <g class="brand-name">
    <text class="label-type maker-name" x="656" y="343" text-anchor="middle">VERDAM</text>
    <text class="label-type product-name" x="656" y="488" text-anchor="middle">FOUNDRY</text>
    <text class="label-type product-kind" x="660" y="582" text-anchor="middle">GIN</text>
  </g>
</svg>
</body>
</html>
```